Cosmetic Dentist Practice needs stationery package/logo

I need a letterhead, envelope and business card for a cosmetic and Dental Inplant practice in an upscale part of Houston. The business card will be a size 3.5 x 2 and the letterhead will be 8.5" x 11" with a standard #10 envelope.
I have uploaded a file with an idea that the dentist had for his cards. Please note that this is not the size that the card should be. It does provide the information required.
Updates
Thank you all for your submissions. They were each unique and special in their own way. My client has made a selection that he feels best meets his needs. I appreciate each of you taking the time to offer designs. Good luck to each of you...I hope to see you back in MarblePost on future projects.
Industry/Entity Type
Business
Look and feel
Each slider illustrates characteristics of the customer's brand and the style your logo design should communicate.

```html
<!DOCTYPE html>
<html lang="en">
<head>
<meta charset="utf-8">
<title>Midtown Smile &amp; Implant Studio — Stationery</title>
<link href="https://fonts.googleapis.com/css2?family=Roboto+Condensed:wght@300;400;700&display=swap" rel="stylesheet">
<style>
  :root {
    --brand-blue: #0d4ea6;
    --paper: #ffffff;
    --backdrop: #e9e9e9;
    --ink-grey: #5a5a5a;
    --band-text: #ffffff;
    --sheet-edge: rgba(0, 0, 0, 0.12);
    --sheet-shadow: 0 3px 7px rgba(0, 0, 0, 0.35);
  }
  * { margin: 0; padding: 0; box-sizing: border-box; }
  html, body { width: 1200px; height: 1000px; overflow: hidden; }
  body {
    position: relative;
    background: var(--backdrop);
    font-family: "Roboto Condensed", "Arial Narrow", sans-serif;
  }

  .letterhead,
  .envelope {
    position: absolute;
    background: var(--paper);
    border: 1px solid var(--sheet-edge);
    box-shadow: var(--sheet-shadow);
  }
  .letterhead {
    left: 69px; top: 34px;
    width: 720px; height: 931px;
  }
  .envelope {
    left: 390px; top: 396px;
    width: 768px; height: 335px;
  }

  .brand {
    position: absolute;
    color: var(--brand-blue);
    font-weight: 700;
    text-transform: uppercase;
  }
  .brand__dot {
    display: block;
    border-radius: 50%;
    background: var(--brand-blue);
  }
  .letterhead .brand { left: 35px; top: 29px; font-size: 27px; line-height: 29px; }
  .letterhead .brand__dot { width: 58px; height: 58px; margin: 0 0 26px 66px; }
  .envelope .brand { left: 26px; top: 24px; font-size: 13.5px; line-height: 14px; }
  .envelope .brand__dot { width: 30px; height: 30px; margin: 0 0 17px 32px; }

  .contact-band {
    position: absolute;
    left: 0; bottom: 0;
    width: 100%; height: 82px;
    background: var(--brand-blue);
    color: var(--band-text);
    text-align: center;
    font-weight: 300;
    font-size: 17px;
    padding-top: 11px;
    line-height: 22px;
  }
  .contact-line { display: flex; justify-content: center; gap: 30px; }
  .contact-item { display: inline-flex; align-items: center; gap: 5px; }
  .contact-item svg { fill: currentColor; }

  .return-address {
    position: absolute;
    left: 29px; top: 281px;
    color: var(--ink-grey);
    font-style: normal;
    font-weight: 300;
    font-size: 11px;
    line-height: 17px;
  }
  .return-address .contact-line { justify-content: flex-start; gap: 18px; }
  .return-address .contact-item { gap: 3px; }
</style>
</head>
<body>

  <section class="letterhead" aria-label="Letterhead">
    <div class="brand">
      <span class="brand__dot"></span>
      Midtown Smile<br>&amp; Implant Studio
    </div>
    <footer class="contact-band">
      <div>84, Linden Crest Drive Suite 210E. Houston, TX. 77098</div>
      <div class="contact-line">
        <span class="contact-item">
          <svg width="20" height="14" viewBox="0 0 20 14" aria-hidden="true"><path d="M1 5c0-3 4-4 9-4s9 1 9 4l-4 1-1-2c-2-1-6-1-8 0L5 6 1 5z"/><path d="M4 13l2-6h8l2 6z"/><circle cx="10" cy="10" r="1.8" fill="#0d4ea6"/></svg>
          555 010 4821
        </span>
        <span class="contact-item">
          <svg width="18" height="15" viewBox="0 0 18 15" aria-hidden="true"><rect x="4" y="0" width="10" height="5"/><rect x="0" y="6" width="18" height="6" rx="1"/><rect x="3" y="12" width="12" height="3"/></svg>
          555 010 4830
        </span>
      </div>
    </footer>
  </section>

  <section class="envelope" aria-label="Envelope">
    <div class="brand">
      <span class="brand__dot"></span>
      Midtown Smile<br>&amp; Implant Studio
    </div>
    <address class="return-address">
      <div>84, Linden Crest Drive Suite 210E. Houston, TX. 77098</div>
      <div class="contact-line">
        <span class="contact-item">
          <svg width="15" height="10" viewBox="0 0 20 14" aria-hidden="true"><path d="M1 5c0-3 4-4 9-4s9 1 9 4l-4 1-1-2c-2-1-6-1-8 0L5 6 1 5z"/><path d="M4 13l2-6h8l2 6z"/><circle cx="10" cy="10" r="1.8" fill="#fff"/></svg>
          555 010 4821
        </span>
        <span class="contact-item">
          <svg width="12" height="10" viewBox="0 0 18 15" aria-hidden="true"><rect x="4" y="0" width="10" height="5"/><rect x="0" y="6" width="18" height="6" rx="1"/><rect x="3" y="12" width="12" height="3"/></svg>
          555 010 4830
        </span>
      </div>
    </address>
  </section>

</body>
</html>
```